Website design for management consulting firm

We need a web design for a new consulting company based in Boston, MA called "Fernhollow Ridge Consulting." This webpage will be simple home page, with a "contact us" page, that describes the services of the consulting firm. The company provides strategic planning, business assessment, process re-designs, and other management consulting functions. I would like the website to look high-tech. A logo was already created via Pixel Harbor.

Target Market(s)

Other business owners across a wide spectrum of industries - from IT to retail.

Industry/Entity Type

It Company

Number of Pages Required

3 page

Colors
0455a3
ffffff

Requirements
Must have
• Front page that provides generic text / overview of the firm. A "services" tab that describes consulting services. A "contact us" tab that provides either a form to contact us or just the contact email address of the company. info@fernhollowridgeconsulting.example

```html
<!DOCTYPE html>
<html lang="en">
<head>
<meta charset="utf-8">
<title>Fernhollow Ridge Consulting</title>
<link rel="stylesheet" href="https://fonts.googleapis.com/css2?family=Raleway:wght@500;600&family=Source+Sans+3:wght@400;600&display=swap">
<style>
:root{
  --page-bg:#333333;
  --white:#ffffff;
  --ink:#222222;
  --brand-blue:#0455a3;
  --teal:#1aa89a;
  --nav-home:#0a1f6b;
  --nav-about:#7a0fe0;
  --nav-services:#ff9500;
  --nav-contact:#3d3d3d;
  --tile-news:#22c322;
  --tile-welcome:#ddae00;
  --tile-about:#e05c03;
  --tile-services:#7600e0;
  --tile-testimonials:#04a0e0;
  --tile-newsletter:#1bb300;
  --tile-follow:#7b300a;
  --tile-contact:#d4190c;
  --footer:#135a8a;
  --head-font:"Raleway",sans-serif;
  --body-font:"Source Sans 3",sans-serif;
}
*{box-sizing:border-box;margin:0;padding:0}
html,body{width:1044px;height:1200px;overflow:hidden}
body{background:var(--page-bg);position:relative;font-family:var(--body-font);color:var(--white)}
.block{position:absolute}

/* header */
.site-header{left:41px;top:2px;width:963px;height:82px;background:var(--white);border-bottom:3px solid #2a2a2a}
.brand{position:absolute;left:12px;top:12px;display:flex;align-items:center;gap:12px}
.brand-mark{width:52px;height:54px;background:var(--brand-blue)}
.brand-name{font-family:var(--head-font);font-weight:600;font-size:22px;color:var(--ink)}
.main-nav{position:absolute;right:0;top:0;height:80px;display:flex}
.main-nav a{display:flex;align-items:center;justify-content:center;height:80px;color:var(--white);text-decoration:none;font-size:11px}
.nav-home{width:67px;background:var(--nav-home)}
.nav-about{width:90px;background:var(--nav-about)}
.nav-services{width:76px;background:var(--nav-services)}
.nav-contact{width:97px;background:var(--nav-contact)}

/* hero */
.hero{left:41px;top:87px;width:962px;height:469px;background:linear-gradient(110deg,#e7d2c6 0%,#d9d9db 30%,#b9bcc2 55%,#dfe3e7 80%,#9fa4ab 100%)}
.hero-panel{position:absolute;left:219px;top:160px;width:580px;height:249px;background:rgba(34,34,34,.88);text-align:center}
.hero-title{font-family:var(--head-font);font-weight:500;font-size:38px;line-height:47px;margin-top:28px}
.hero-title .accent{display:block;color:var(--teal)}
.hero-text{font-size:11px;line-height:18px;margin:16px 36px 0}
.read-more{display:inline-block;margin-top:14px;width:91px;height:29px;line-height:29px;background:var(--teal);font-size:11px;color:var(--white);text-decoration:none}
.hero-arrow{position:absolute;top:193px;width:35px;height:35px}
.hero-arrow.prev{left:11px}
.hero-arrow.next{right:18px}

/* tiles */
.tile{position:absolute;text-align:center}
.tile-icon{position:absolute;left:50%;transform:translateX(-50%);width:78px;height:78px}
.tile-label{position:absolute;left:0;right:0;font-family:var(--head-font);font-weight:500;font-size:20px}
.row-one .tile-icon{top:32px}
.row-one .tile-label{top:127px}
.row-two .tile-icon{top:38px}
.row-two .tile-label{top:124px}
.news{left:41px;top:559px;width:318px;height:198px;background:var(--tile-news)}
.welcome{left:362px;top:559px;width:319px;height:198px;background:var(--tile-welcome)}
.about{left:684px;top:559px;width:319px;height:198px;background:var(--tile-about)}
.services{left:41px;top:760px;width:351px;height:194px;background:var(--tile-services)}
.testimonials{left:395px;top:760px;width:262px;height:194px;background:var(--tile-testimonials)}
.newsletter{left:659px;top:760px;width:344px;height:194px;background:var(--tile-newsletter)}
.welcome-title{font-family:var(--head-font);font-weight:500;font-size:25px;line-height:29px;margin-top:22px}
.welcome-text{font-size:10.5px;line-height:14px;text-align:justify;margin:8px 21px 0}
.welcome-arrow{position:absolute;left:263px;top:150px;width:31px;height:31px}

.follow{left:41px;top:958px;width:489px;height:176px;background:var(--tile-follow)}
.contact{left:533px;top:958px;width:470px;height:176px;background:var(--tile-contact)}
.band-title{position:absolute;left:0;right:0;top:40px;font-family:var(--head-font);font-weight:500;font-size:20px}
.follow .band-title{left:0;right:0;width:438px}
.contact .band-title{width:432px}
.icon-row{position:absolute;top:88px;display:flex}
.follow .icon-row{left:125px;gap:20px}
.contact .icon-row{left:127px;top:84px;gap:33px}
.social{width:47px;height:47px;border:1px solid var(--white);border-radius:50%}
.social.solid{background:var(--white)}
.contact-icon{width:50px;height:50px}

.site-footer{left:41px;top:1138px;width:962px;height:62px;background:var(--footer);text-align:center;font-size:10.5px;line-height:50px}
</style>
</head>
<body>

<header class="block site-header">
  <div class="brand">
    <span class="brand-mark"></span>
    <span class="brand-name">Fernhollow Ridge Consulting</span>
  </div>
  <nav class="main-nav">
    <a class="nav-home" href="#">Home</a>
    <a class="nav-about" href="#">About Us</a>
    <a class="nav-services" href="#">Services</a>
    <a class="nav-contact" href="#">Contact Us</a>
  </nav>
</header>

<section class="block hero" role="img" aria-label="Photo of a hand on a computer mouse beside a keyboard on a desk">
  <div class="hero-panel">
    <h1 class="hero-title">CHANGE YOUR FUTURE <span class="accent">BE SUCCESSFUL</span></h1>
    <p class="hero-text">Lorem ipsum dolor sit amet, consectetur adipiscing elit, sed do eiusmod tempor incididunt ut labore et dolore magna aliqua. Ut enim ad minim veniam, quis nostrud exercitation ullamco laborisLorem ipsum dolor sit amet, consectetur adipiscing elit, sed do eiusmod tempor incididunt ut labore</p>
    <a class="read-more" href="#">READ MORE</a>
    <svg class="hero-arrow prev" viewBox="0 0 36 36"><circle cx="18" cy="18" r="16.5" fill="none" stroke="#fff" stroke-width="2"/><path d="M20 12l-6 6 6 6" fill="none" stroke="#fff" stroke-width="2"/></svg>
    <svg class="hero-arrow next" viewBox="0 0 36 36"><circle cx="18" cy="18" r="16.5" fill="none" stroke="#fff" stroke-width="2"/><path d="M16 12l6 6-6 6" fill="none" stroke="#fff" stroke-width="2"/></svg>
  </div>
</section>

<div class="row-one">
  <a class="tile news">
    <svg class="tile-icon" viewBox="0 0 78 78"><circle cx="39" cy="39" r="38" fill="none" stroke="#fff" stroke-width="1"/><path d="M28 24h16l7 7v23H28z" fill="none" stroke="#fff" stroke-width="2.5"/><path d="M33 37h13M33 42h13M33 47h13" stroke="#fff" stroke-width="2.5"/></svg>
    <span class="tile-label">Latest News</span>
  </a>
  <div class="tile welcome">
    <h2 class="welcome-title">WELCOME TO<br>FERNHOLLOW RIDGE</h2>
    <p class="welcome-text">Lorem ipsum dolor sit amet, consectetur adipiscing elit, sed do eiusmod tempor incididunt ut labore et dolore magna aliqua. onsectetur adipiscing elit, sed do eiusmod ut labore et dolore magna aliqua.</p>
    <svg class="welcome-arrow" viewBox="0 0 32 32"><circle cx="16" cy="16" r="15" fill="none" stroke="#fff"/><path d="M14 10l6 6-6 6" fill="none" stroke="#fff" stroke-width="1.5"/></svg>
  </div>
  <a class="tile about">
    <svg class="tile-icon" viewBox="0 0 78 78"><circle cx="39" cy="39" r="38" fill="none" stroke="#fff" stroke-width="1"/><g fill="#fff"><path d="M39 26l8 4v8l-8 4-8-4v-8z"/><path d="M30 39l8 4v8l-8 4-8-4v-8z"/><path d="M48 39l8 4v8l-8 4-8-4v-8z"/></g></svg>
    <span class="tile-label">About Us</span>
  </a>
</div>

<div class="row-two">
  <a class="tile services">
    <svg class="tile-icon" viewBox="0 0 78 78"><circle cx="39" cy="39" r="38" fill="none" stroke="#fff" stroke-width="1"/><path d="M28 24h16l7 7v23H28z" fill="none" stroke="#fff" stroke-width="2.5"/><path d="M33 37h13M33 42h13M33 47h13" stroke="#fff" stroke-width="2.5"/></svg>
    <span class="tile-label">Services</span>
  </a>
  <a class="tile testimonials">
    <svg class="tile-icon" viewBox="0 0 78 78"><circle cx="39" cy="39" r="38" fill="none" stroke="#fff" stroke-width="1"/><circle cx="39" cy="32" r="7" fill="#fff"/><path d="M26 52c0-9 6-12 13-12s13 3 13 12z" fill="#fff"/></svg>
    <span class="tile-label">Testimonials</span>
  </a>
  <a class="tile newsletter">
    <svg class="tile-icon" viewBox="0 0 78 78"><circle cx="39" cy="39" r="38" fill="none" stroke="#fff" stroke-width="1"/><path d="M54 24L22 39l10 4 3 12 6-8 9 5z" fill="#fff"/><path d="M32 43l20-17-15 20" fill="none" stroke="#1bb300" stroke-width="2"/></svg>
    <span class="tile-label">Our Newsletter</span>
  </a>
</div>

<section class="tile follow">
  <h2 class="band-title">Follow Us</h2>
  <div class="icon-row" aria-label="Social profiles">
    <span class="social solid"></span>
    <span class="social"></span>
    <span class="social"></span>
  </div>
</section>

<section class="tile contact">
  <h2 class="band-title">Contact Us</h2>
  <div class="icon-row">
    <svg class="contact-icon" viewBox="0 0 50 50" aria-label="Phone"><circle cx="25" cy="25" r="24" fill="none" stroke="#fff"/><path d="M19 16l4 4-2 3c1 3 3 5 6 6l3-2 4 4-3 3c-7 0-15-8-15-15z" fill="#fff"/></svg>
    <svg class="contact-icon" viewBox="0 0 50 50" aria-label="Fax"><circle cx="25" cy="25" r="24" fill="none" stroke="#fff"/><rect x="16" y="20" width="4" height="14" fill="#fff"/><rect x="21" y="16" width="13" height="18" rx="1" fill="#fff"/><g fill="#d4190c"><rect x="23" y="18" width="9" height="4"/><rect x="23" y="24" width="2" height="2"/><rect x="27" y="24" width="2" height="2"/><rect x="31" y="24" width="2" height="2"/><rect x="23" y="28" width="2" height="2"/><rect x="27" y="28" width="2" height="2"/><rect x="31" y="28" width="2" height="2"/></g></svg>
    <svg class="contact-icon" viewBox="0 0 50 50" aria-label="Email info@fernhollowridgeconsulting.example"><circle cx="25" cy="25" r="24" fill="none" stroke="#fff"/><rect x="15" y="18" width="20" height="14" rx="2" fill="none" stroke="#fff" stroke-width="2"/><path d="M15 19l10 8 10-8" fill="none" stroke="#fff" stroke-width="2"/></svg>
  </div>
</section>

<footer class="block site-footer">All Right Reserved. Copyright ©2015 Company Name</footer>

</body>
</html>
```